Local Horticulturalist needs Business card design

Meridale Gardening would like to update our existing business card and utilize our new logo (design attached)....we specialize in getting the best out of our customers yard with professional maintenance programs, expert pruning and hedging and garden restorations.
Utilizing colors from attached logo I would like a design that implies professionalism and if possible our businesses love of restoration through plants.
I also sometimes write down for my customers a start date and price on the back of my current card
Target Market(s)
Home owners
Contractors
Industry/Entity Type
Gardener
Contact Information for Business Card
Trevor Kalbrook | Horticulturalist
ph: 0452739186
meridalegard@fernpost.com
www.meridalegardening.com.au
Requirements
Must have
- crucial information easy to read
- incorporate current logo
- Horticulturalist listed preferably near name
Nice to have
- currently I write a job start date and price on the back of my current card so something that integrates this would be beneficial
Should not have
- be pretty or flowerey
- be too white or basic

```html
<!DOCTYPE html>
<html lang="en">
<head>
<meta charset="utf-8">
<title>Meridale Gardening – Business Card</title>
<link rel="stylesheet" href="https://fonts.googleapis.com/css2?family=Open+Sans:wght@400;600;700&display=swap">
<style>
  :root {
    --page: #ecebe7;
    --charcoal: #3c3c3d;
    --leaf: #84b83f;
    --soil: #7b6d57;
    --paper: #ffffff;
    --paper-shade: #eeeeee;
    --ink-light: #f4f4f4;
    --field-ink: #e8e8e8;
  }
  * { box-sizing: border-box; margin: 0; padding: 0; }
  html, body { width: 1200px; height: 900px; overflow: hidden; }
  body {
    background: var(--page);
    font-family: "Open Sans", Arial, sans-serif;
    position: relative;
  }
  .card {
    position: absolute;
    width: 500px;
    height: 286px;
    border-radius: 3px;
    overflow: hidden;
    box-shadow: 0 10px 24px rgba(0,0,0,.18);
  }
  /* back of card */
  .card--back {
    left: 90px; top: 150px;
    background: var(--charcoal);
  }
  .brand {
    position: absolute;
    display: flex;
    align-items: center;
    gap: 12px;
  }
  .brand__dot {
    border-radius: 50%;
    background: var(--leaf);
    flex: none;
  }
  .brand__name {
    font-weight: 700;
    color: var(--leaf);
    line-height: 1;
    white-space: nowrap;
  }
  .brand__tagline {
    font-weight: 600;
    color: var(--soil);
    line-height: 1.2;
    white-space: nowrap;
  }
  .card--back .brand { left: 48px; top: 74px; }
  .card--back .brand__dot { width: 56px; height: 56px; }
  .card--back .brand__name { font-size: 30px; }
  .card--back .brand__tagline { font-size: 14px; margin-top: 4px; }

  .job-field {
    position: absolute;
    color: var(--field-ink);
    font-size: 15px;
    display: flex;
    align-items: flex-end;
    gap: 3px;
  }
  .job-field__line {
    display: inline-block;
    border-bottom: 1px solid var(--field-ink);
    height: 1px;
    margin-bottom: 4px;
  }
  .job-field--price { right: 40px; top: 168px; }
  .job-field--price .job-field__line { width: 95px; }
  .job-field--start { left: 50px; top: 222px; }
  .job-field--start .job-field__line { width: 105px; }

  /* front of card */
  .card--front {
    left: 610px; top: 460px;
    background: linear-gradient(180deg, var(--paper) 0%, var(--paper-shade) 55%);
  }
  .card--front .brand { left: 112px; top: 44px; gap: 8px; }
  .card--front .brand__dot { width: 44px; height: 44px; }
  .card--front .brand__name { font-size: 22px; }
  .card--front .brand__tagline { font-size: 11px; margin-top: 3px; }

  .contact-band {
    position: absolute;
    left: 0; right: 0; top: 132px; height: 130px;
    background: var(--leaf);
  }
  .card--front .base-strip {
    position: absolute;
    left: 0; right: 0; bottom: 0; height: 24px;
    background: var(--soil);
  }
  .holder {
    position: absolute;
    left: 28px; top: 54px;
    color: var(--ink-light);
  }
  .holder__name { font-size: 26px; font-weight: 600; line-height: 1.1; }
  .holder__role { font-size: 15px; text-align: right; }

  .contact-list {
    position: absolute;
    left: 272px; top: 10px;
    list-style: none;
    color: var(--ink-light);
    font-size: 12.5px;
  }
  .contact-list li {
    display: flex;
    align-items: center;
    gap: 7px;
    height: 21px;
    white-space: nowrap;
  }
  .contact-list svg { width: 14px; height: 14px; flex: none; }
</style>
</head>
<body>

  <section class="card card--back" aria-label="Card back">
    <div class="brand">
      <span class="brand__dot"></span>
      <div>
        <div class="brand__name">Meridale Gardening</div>
        <div class="brand__tagline">Garden Restorations &amp;Maintenance</div>
      </div>
    </div>
    <div class="job-field job-field--price">Price:<span class="job-field__line"></span></div>
    <div class="job-field job-field--start">Start Date:<span class="job-field__line"></span></div>
  </section>

  <section class="card card--front" aria-label="Card front">
    <div class="brand">
      <span class="brand__dot"></span>
      <div>
        <div class="brand__name">Meridale Gardening</div>
        <div class="brand__tagline">Garden Restorations &amp;Maintenance</div>
      </div>
    </div>

    <div class="contact-band">
      <div class="holder">
        <div class="holder__name">Trevor Kalbrook</div>
        <div class="holder__role">Horticulturalist</div>
      </div>
      <ul class="contact-list">
        <li>
          <svg viewBox="0 0 14 14" aria-hidden="true"><rect width="14" height="14" rx="2" fill="#fff"/><path d="M3 5.2 Q3 3.5 4.6 3.5 L9.4 3.5 Q11 3.5 11 5.2 L9.4 5.6 L9 4.8 L5 4.8 L4.6 5.6 Z M4.6 6.4 L9.4 6.4 L10.5 10.5 L3.5 10.5 Z" fill="#84b83f"/></svg>
          0452739186
        </li>
        <li>
          <svg viewBox="0 0 14 14" aria-hidden="true"><rect width="14" height="14" rx="2" fill="#fff"/><rect x="3" y="4" width="8" height="6" fill="none" stroke="#84b83f" stroke-width="1.2"/><path d="M3 4 L7 7.5 L11 4" fill="none" stroke="#84b83f" stroke-width="1.2"/></svg>
          meridalegard@fernpost.com
        </li>
        <li>
          <svg viewBox="0 0 14 14" aria-hidden="true"><rect width="14" height="14" rx="2" fill="#fff"/><path d="M4 10 L10 4 M5.5 5.5 L7 4 Q8.5 2.8 10 4 Q11.2 5.5 10 7 L8.5 8.5 M5.5 5.5 L4 7 Q2.8 8.5 4 10 Q5.5 11.2 7 10 L8.5 8.5" fill="none" stroke="#84b83f" stroke-width="1.2"/></svg>
          www.meridalegardening.com.au
        </li>
      </ul>
    </div>
    <div class="base-strip"></div>
  </section>

</body>
</html>
```